WP website design for Pelton

We need a wordpress design that will incorporate a professional color scheme with company logo in a clean layout. The design needs to consider that this will be developed on a responsive theme. Colors are will be the green of the logo and any others that will creatively highlight it.

Industry/Entity Type

It Company

Font styles to use
Sans Serif

Requirements
Must have
• Navigation: 1) Home 2) Auctions 3) Auction Services 4) Sellers 5) RK Pelton Livestock 6) About Us 7) Contact Us
Site will have slideshow element, image attached.
Widgets will be: 1)Email Signup form 2) Featured Auctions widget 3) Social Media (Chirply, Vidloop, RSS) 4) News & Events blog
Footer will have smaller company logo, association logos (attached) and contact info (below)
▪ R.K. Pelton Inc. / Auctioneers
▪ 4716 NC Hwy 91
▪ Marbury, NC 27604
▪ Office: (252) 555-0184
▪ Cell: (252) 555-0137
▪ email: rkpelton@rkpelton-example.com
Nice to have
• Site will have drop-down menus - please indicate the styling, for instance the dropdown menus

```html
<!DOCTYPE html>
<html lang="en">
<head>
<meta charset="utf-8">
<title>R.K. Pelton Inc. / Auctioneers</title>
<link rel="stylesheet" href="https://fonts.googleapis.com/css2?family=Gelasio:wght@400;700&display=swap">
<style>
:root{
  --green:#358a1a;
  --green-dark:#2c7a14;
  --text:#222;
  --muted:#666;
  --panel:#f4f4f4;
  --line:#e2e2e2;
  --page:#ececec;
  --white:#fff;
  --dark:#2b2b2b;
}
*{box-sizing:border-box;margin:0;padding:0}
html,body{width:976px;height:1200px;overflow:hidden}
body{font-family:"Gelasio",Georgia,serif;color:var(--text);background:var(--page);position:relative}
.top-band{position:absolute;left:0;top:0;width:976px;height:398px;background:var(--green)}
.header{position:absolute;left:118px;top:26px;width:740px;height:76px;background:var(--white)}
.brand{position:absolute;left:22px;top:22px;display:flex;align-items:center;gap:7px;color:var(--green);font-size:15px}
.brand .mark{width:22px;height:22px;border-radius:50%;background:var(--green)}
.brand small{display:block;font-size:9px;margin-top:2px}
.nav{position:absolute;right:14px;top:31px;display:flex;gap:16px;font-size:12.5px;color:var(--green);white-space:nowrap}
.slider{position:absolute;left:118px;top:102px;width:740px;height:276px;background:linear-gradient(#c9d6e0 0%,#a9a27a 22%,#5e6b3a 40%,#c98a38 55%,#8d7a5a 68%,#a58a64 85%,#7a6a55 100%)}
.dots{position:absolute;left:340px;bottom:14px;display:flex;gap:6px}
.dots span{width:11px;height:11px;border-radius:50%;background:var(--white)}
.dots span.on{background:var(--green)}
.content{position:absolute;left:118px;top:398px;width:740px;height:676px;background:var(--white);box-shadow:0 1px 3px rgba(0,0,0,.12)}
h2{font-weight:400;font-size:17.5px;color:var(--text)}
.featured-title{position:absolute;left:23px;top:24px}
.arrows{position:absolute;left:462px;top:26px;display:flex;gap:8px}
.auction{position:absolute;left:22px;width:466px;height:193px;background:var(--panel);border:1px solid var(--line);box-shadow:0 1px 2px rgba(0,0,0,.1)}
.auction-head{position:absolute;left:12px;top:19px;font-size:10px;letter-spacing:.3px}
.actions{position:absolute;right:17px;top:12px;display:flex;gap:6px}
.btn{display:flex;align-items:center;gap:8px;height:23px;padding:0 9px 0 8px;background:var(--green);color:var(--white);font-size:9.5px}
.btn svg{width:11px;height:11px}
.auction-body{position:absolute;left:14px;top:42px;width:440px;height:135px;background:var(--white);border:1px solid var(--line)}
.auction-photo{position:absolute;left:15px;top:11px;width:113px;height:110px}
.auction-info{position:absolute;left:141px;top:14px;font-size:7.4px;line-height:15.3px;width:295px;white-space:nowrap}
.auction-info p+p{margin-top:15px}
.side{position:absolute;left:503px;width:217px}
.blog-title{top:22px}
.blog-photo{position:absolute;left:503px;top:61px;width:217px;height:154px;background:linear-gradient(#5a8a3a 0%,#3f7a28 30%,#2f9a2c 55%,#6d8f4a 80%,#8ea86a 100%)}
.blog-lead{position:absolute;left:503px;top:223px;width:217px;font-size:9px;line-height:17px;color:var(--green)}
.blog-text{position:absolute;left:503px;top:262px;width:217px;font-size:9px;line-height:17px}
.read-more{position:absolute;left:503px;top:336px;width:67px;height:23px;background:var(--green);color:var(--white);font-size:9.5px;display:flex;align-items:center;justify-content:center}
.signup{position:absolute;left:503px;top:375px;width:217px;height:179px;background:var(--panel)}
.signup h2{position:absolute;left:12px;top:13px}
.signup p{position:absolute;left:12px;top:42px;width:195px;font-size:9px;line-height:16px}
.field{position:absolute;left:12px;width:195px;height:25px;background:var(--white);border:1px solid #ddd;font-size:9px;color:#999;padding:7px 0 0 10px}
.signup-btn{position:absolute;left:12px;top:144px;width:71px;height:23px;background:var(--dark);color:var(--white);font-size:9.5px;display:flex;align-items:center;justify-content:center}
.connect{position:absolute;left:505px;top:573px}
.social{position:absolute;left:506px;top:606px;display:flex;gap:6px}
.social span{width:34px;height:34px;border-radius:50%;background:var(--green);color:var(--white);font-size:6.5px;display:flex;align-items:center;justify-content:center}
.footer{position:absolute;left:0;top:1093px;width:976px;height:107px;background:var(--white)}
.footer-brand{position:absolute;left:125px;top:30px;display:flex;align-items:center;gap:7px;color:var(--green);font-size:14px}
.footer-brand .mark{width:20px;height:20px;border-radius:50%;background:var(--green)}
.footer-brand small{display:block;font-size:8.5px;margin-top:2px;color:var(--muted)}
.contact-label{position:absolute;left:262px;top:38px;font-size:12.5px;color:var(--green)}
.divider{position:absolute;left:346px;top:12px;width:1px;height:76px;background:var(--dark)}
.divider-arrow{position:absolute;left:347px;top:39px;width:0;height:0;border-left:5px solid var(--dark);border-top:4px solid transparent;border-bottom:4px solid transparent}
.address{position:absolute;left:372px;top:14px;font-size:9.5px;line-height:17px}
.address .co{color:var(--green)}
.phones{position:absolute;left:517px;top:15px;font-size:9.5px;line-height:17px}
.emails{position:absolute;left:373px;top:72px;font-size:9.5px;white-space:nowrap}
.assoc{position:absolute;left:688px;top:13px;font-size:12px;color:var(--green)}
.badges{position:absolute;left:686px;top:37px;display:flex;gap:10px;align-items:center}
</style>
</head>
<body>
<div class="top-band"></div>

<header class="header">
  <div class="brand"><span class="mark"></span><div>R.K. Pelton<small>Inc. / Auctioneers</small></div></div>
  <nav class="nav"><span>Home</span><span>Auctions</span><span>Auction Services</span><span>Sellers</span><span>RK Pelton Livestock</span><span>About Us</span><span>Contact Us</span></nav>
</header>

<section class="slider" role="img" aria-label="Slideshow photo of autumn trees and a golden field reflected in a pond">
  <div class="dots"><span class="on"></span><span></span><span></span><span></span></div>
</section>

<main class="content">
  <h2 class="featured-title">Featured Auctions</h2>
  <div class="arrows">
    <svg width="10" height="14" viewBox="0 0 10 14"><path d="M8 1 2 7l6 6" fill="none" stroke="#555" stroke-width="1.5"/></svg>
    <svg width="10" height="14" viewBox="0 0 10 14"><path d="M2 1l6 6-6 6" fill="none" stroke="#555" stroke-width="1.5"/></svg>
  </div>

  <article class="auction" style="top:63px">
    <div class="auction-head">AUCTIONS 1</div>
    <div class="actions">
      <span class="btn"><svg viewBox="0 0 12 12"><rect x="1" y="2" width="10" height="8" fill="none" stroke="#fff"/><circle cx="6" cy="6" r="2" fill="none" stroke="#fff"/></svg>Photos</span>
      <span class="btn"><svg viewBox="0 0 12 12"><rect x="1" y="1.5" width="10" height="9" fill="none" stroke="#fff"/><path d="M3.5 1.5v9M8.5 1.5v9" stroke="#fff"/></svg>Videos</span>
      <span class="btn"><svg viewBox="0 0 12 12"><path d="M2.5 1h5l2 2v8h-7z" fill="none" stroke="#fff"/><path d="M4 5h4M4 7h4M4 9h4" stroke="#fff"/></svg>Details</span>
    </div>
    <div class="auction-body">
      <div class="auction-photo" role="img" aria-label="Photo of a green farm tractor on grass" style="background:linear-gradient(#8fb0c8 0%,#5d8a3c 35%,#2f7a24 60%,#6a9a3a 100%)"></div>
      <div class="auction-info">
        <p><b>Begins:</b> Saturday, September 20, 2014 at 10:00 AM EDT<br><b>Location:</b> 2281 Millbrook Rd. Marbury, NC 27604</p>
        <p>FR 2950, Tarrow Mule, Broadfield 10' no till drill. 20' Alum stock trl, 28'<br>alum gooseneck F Kessler 504 baler, HL 275 baler, Kessler TM800 disc<br>mower, creep feeders, WW panels<br>(6) Angus X &amp; (4) Simm X cows, (9) calves, Simm. bull</p>
      </div>
    </div>
  </article>

  <article class="auction" style="top:263px">
    <div class="auction-head">AUCTIONS 1</div>
    <div class="actions">
      <span class="btn"><svg viewBox="0 0 12 12"><rect x="1" y="2" width="10" height="8" fill="none" stroke="#fff"/><circle cx="6" cy="6" r="2" fill="none" stroke="#fff"/></svg>Photos</span>
      <span class="btn"><svg viewBox="0 0 12 12"><rect x="1" y="1.5" width="10" height="9" fill="none" stroke="#fff"/><path d="M3.5 1.5v9M8.5 1.5v9" stroke="#fff"/></svg>Videos</span>
      <span class="btn"><svg viewBox="0 0 12 12"><path d="M2.5 1h5l2 2v8h-7z" fill="none" stroke="#fff"/><path d="M4 5h4M4 7h4M4 9h4" stroke="#fff"/></svg>Details</span>
    </div>
    <div class="auction-body">
      <div class="auction-photo" role="img" aria-label="Photo of a brown cow standing in a green pasture" style="background:linear-gradient(90deg,#4a8a2a 0%,#5a3a24 30%,#4a2e1c 65%,#4f8f2e 100%)"></div>
      <div class="auction-info">
        <p><b>Begins:</b> Saturday, September 20, 2014 at 10:00 AM EDT<br><b>Location:</b> 2281 Millbrook Rd. Marbury, NC 27604</p>
        <p>FR 2950, Tarrow Mule, Broadfield 10' no till drill. 20' Alum stock trl, 28'<br>alum gooseneck F Kessler 504 baler, HL 275 baler, Kessler TM800 disc<br>mower, creep feeders, WW panels<br>(6) Angus X &amp; (4) Simm X cows, (9) calves, Simm. bull</p>
      </div>
    </div>
  </article>

  <article class="auction" style="top:464px">
    <div class="auction-head">AUCTIONS 1</div>
    <div class="actions">
      <span class="btn"><svg viewBox="0 0 12 12"><rect x="1" y="2" width="10" height="8" fill="none" stroke="#fff"/><circle cx="6" cy="6" r="2" fill="none" stroke="#fff"/></svg>Photos</span>
      <span class="btn"><svg viewBox="0 0 12 12"><rect x="1" y="1.5" width="10" height="9" fill="none" stroke="#fff"/><path d="M3.5 1.5v9M8.5 1.5v9" stroke="#fff"/></svg>Videos</span>
      <span class="btn"><svg viewBox="0 0 12 12"><path d="M2.5 1h5l2 2v8h-7z" fill="none" stroke="#fff"/><path d="M4 5h4M4 7h4M4 9h4" stroke="#fff"/></svg>Details</span>
    </div>
    <div class="auction-body">
      <div class="auction-photo" role="img" aria-label="Photo of black cattle grazing in a fenced pasture" style="background:linear-gradient(#8aa870 0%,#5a9a3a 25%,#2a2622 45%,#262320 70%,#58a03a 100%)"></div>
      <div class="auction-info">
        <p><b>Begins:</b> Saturday, September 20, 2014 at 10:00 AM EDT<br><b>Location:</b> 2281 Millbrook Rd. Marbury, NC 27604</p>
        <p>FR 2950, Tarrow Mule, Broadfield 10' no till drill. 20' Alum stock trl, 28'<br>alum gooseneck F Kessler 504 baler, HL 275 baler, Kessler TM800 disc<br>mower, creep feeders, WW panels<br>(6) Angus X &amp; (4) Simm X cows, (9) calves, Simm. bull</p>
      </div>
    </div>
  </article>

  <h2 class="side blog-title">News &amp; Event Blog</h2>
  <div class="blog-photo" role="img" aria-label="Photo of a green seed drill parked on a grassy field"></div>
  <p class="blog-lead">Lorem Ipsum is simply dummy text of the printing and typesetting industry.</p>
  <p class="blog-text">Lorem Ipsum has been the industry's standard dummy text ever since the 1500s, when an unknown printer took a galley of type and scrambled it to make a type specimen book.</p>
  <span class="read-more">Read More</span>

  <form class="signup">
    <h2>Email Sign-Up</h2>
    <p>Lorem Ipsum is simply dummy text of the printing and typesetting industry.</p>
    <div class="field" style="top:79px">Name</div>
    <div class="field" style="top:111px">E-Mail ID</div>
    <span class="signup-btn">Sign Up</span>
  </form>

  <h2 class="connect">Connect With Us</h2>
  <div class="social">
    <span>Chirply</span>
    <span>Vidloop</span>
    <span><svg width="16" height="16" viewBox="0 0 16 16"><circle cx="3" cy="13" r="2" fill="#fff"/><path d="M1 7a8 8 0 0 1 8 8M1 2a13 13 0 0 1 13 13" fill="none" stroke="#fff" stroke-width="2.2"/></svg></span>
  </div>
</main>

<footer class="footer">
  <div class="footer-brand"><span class="mark"></span><div>R.K. Pelton<small>Inc. / Auctioneers</small></div></div>
  <div class="contact-label">Contact Info</div>
  <div class="divider"></div><div class="divider-arrow"></div>
  <div class="address"><span class="co">R.K. Pelton Inc. / Auctioneers</span><br>4716 NC Hwy 91<br>Marbury, NC 27604</div>
  <div class="phones">(252) 555-0184 6:15 AM - 9:59 PM<br>(252) 555-0137 R.K.'s mobile<br>(252) 555-0162 sale day pager</div>
  <div class="emails">rkpelton@rkpelton-example.com &nbsp;| &nbsp;mara@rkpelton-example.com &nbsp;| &nbsp;dale@rkpelton-example.com</div>
  <div class="assoc">Association</div>
  <div class="badges">
    <svg width="56" height="24" role="img" aria-label="Auctioneers association badge"><rect x="1" y="4" width="54" height="16" rx="3" fill="#ddd"/></svg>
    <svg width="38" height="28" role="img" aria-label="Beef council badge"><rect x="1" y="2" width="36" height="24" rx="4" fill="#e4e4e4" stroke="#c33" stroke-width="1.5"/></svg>
    <svg width="40" height="40" role="img" aria-label="Cattlemen association badge"><circle cx="20" cy="20" r="18" fill="#d9d9d9" stroke="#3a7a2a" stroke-width="2"/></svg>
  </div>
</footer>
</body>
</html>
```